Modernization of existing web site

Update existing web site to a professional look vs a home-made site. Site look and navigation should be up to today's standards and display properly on mobile devices.
Only simple HTML and CSS is to be used as this is a basic site. No content management.
Existing site is https://www.plexumar.example

Target Market(s)

Insurance and Technology

Industry/Entity Type

Insurance and technology

Coding

Coded - Design and coding required

Number of Pages Required

5+ page

Font styles to use
Sans Serif

Colors
0054AA
0677BA
7BADD7
CADEEF
E8F1F8
0094D4
00A9DD
6FCCEA
C7EBF8
E9F6FB

Requirements
Must have
• A sleek, modern feel and also done with a button-downed industry in mind.
Nice to have
• Clean integration of the logo and name
Should not have
• Open to ideas

```html
<!DOCTYPE html>
<html lang="en">
<head>
<meta charset="utf-8">
<title>Plexumar</title>
<link rel="stylesheet" href="https://fonts.googleapis.com/css2?family=Roboto:wght@400;500;700&family=Arimo:wght@400&display=swap">
<style>
:root{
  --blue:#2478c4;
  --blue-deep:#0054AA;
  --ink:#333;
  --text:#555;
  --muted:#777;
  --line:#c9c9c9;
  --pale:#E8F1F8;
  --footer:#232323;
  --white:#fff;
}
*{box-sizing:border-box;margin:0;padding:0}
html,body{width:1200px;height:3429px;overflow:hidden}
body{position:relative;background:var(--white);font-family:'Roboto',sans-serif;color:var(--ink)}
.abs{position:absolute}

/* header */
.site-header{position:absolute;left:0;top:0;width:1200px;height:117px;background:var(--white)}
.brand{position:absolute;left:112px;top:30px;display:flex;align-items:center;gap:10px;color:var(--blue);font-weight:700;font-size:44px;letter-spacing:.5px}
.brand-dot{width:54px;height:54px;border-radius:50%;background:var(--blue)}
.main-nav{position:absolute;top:55px;left:0;width:1200px;font-size:14px;font-weight:500;text-transform:uppercase}
.main-nav a{position:absolute;color:var(--ink);text-decoration:none}
.main-nav a.active{color:var(--blue)}

/* hero */
.hero{position:absolute;left:0;top:117px;width:1200px;height:740px;overflow:hidden}
.hero-photo{position:absolute;inset:0;background:linear-gradient(100deg,#0b1522 0%,#15222f 50%,#1e2a38 75%,#0d1723 100%)}
.hero-curve{position:absolute;left:0;top:0}
.hero-title{position:absolute;left:110px;top:190px;font-size:68px;font-weight:700;color:var(--blue);letter-spacing:.5px}
.hero-sub{position:absolute;left:112px;top:293px;font-size:26px;font-weight:500;color:var(--white);line-height:42px}
.btn{display:block;position:absolute;background:var(--blue);color:var(--white);border-radius:30px;text-align:center;font-weight:500;text-decoration:none;text-transform:uppercase}
.hero .btn{left:112px;top:393px;width:160px;height:57px;line-height:57px;font-size:17px}
.slider-dots{position:absolute;left:576px;top:693px;display:flex;gap:8px}
.slider-dots span{width:10px;height:10px;border-radius:50%;background:var(--blue)}
.slider-dots span.on{background:var(--white)}

/* section headings */
.heading{font-size:36px;font-weight:500;color:var(--ink)}
.heading em{font-style:normal;color:var(--blue)}
.rule{height:3px;width:48px;background:var(--muted)}
.rule.blue{background:var(--blue)}

/* about */
.about-heading{left:112px;top:988px}
.about .rule{left:112px;top:1041px}
.about-copy{left:112px;top:1064px;width:454px;font-family:'Arimo',sans-serif;font-size:13.6px;line-height:25.8px;color:var(--text);text-align:justify}
.about-copy p+p{margin-top:26px}
.about .btn{left:112px;top:1356px;width:151px;height:52px;line-height:52px;font-size:16px}
.portrait-frame{left:600px;top:941px}
.portrait{left:622px;top:961px;width:446px;height:464px;background:linear-gradient(180deg,#8a7d62 0%,#6f6450 60%,#3a3632 100%)}

/* services */
.services{left:0;top:1525px;width:1200px;height:877px;background:
  linear-gradient(90deg,rgba(255,255,255,.65),rgba(255,255,255,.35) 50%,rgba(255,255,255,.6)),
  linear-gradient(180deg,#e3e9ef 0%,#dfe6ee 50%,#e9eef3 100%)}
.services-heading{left:0;top:53px;width:1200px;text-align:center}
.services .rule{left:576px;top:108px}
.services svg{position:absolute;left:0;top:0}
.services text{font-family:'Roboto',sans-serif;font-size:15.5px;font-weight:500;fill:#4a4a4a}

/* contact */
.contact-heading{left:0;top:2448px;width:1200px;text-align:center}
.contact .rule{left:576px;top:2499px}
.contact-intro{left:0;top:2519px;width:1200px;text-align:center;font-family:'Arimo',sans-serif;font-size:13px;line-height:26px;color:var(--muted)}
.field{position:absolute;border:1px solid var(--line);background:var(--white);font-family:'Arimo',sans-serif;font-size:13px;color:#444;padding:0 17px;line-height:48px}
.field.area{line-height:1;padding-top:26px}
.contact .btn{left:525px;top:2952px;width:150px;height:50px;line-height:50px;font-size:16px;border:none}

/* footer */
.site-footer{left:0;top:3052px;width:1200px;height:377px;background:var(--footer);color:var(--white)}
.footer-brand{left:0;top:48px;width:1200px;display:flex;justify-content:center;align-items:center;gap:12px;color:var(--blue);font-size:54px;font-weight:700}
.footer-brand .brand-dot{width:70px;height:70px}
.footer-nav{left:0;top:155px;width:1200px;font-size:14px;font-weight:500}
.footer-nav a{position:absolute;color:var(--white);text-decoration:none}
.info{display:flex;align-items:center;gap:14px;font-size:14.5px;line-height:23px}
.ring{width:44px;height:44px;border:1px solid #bbb;border-radius:50%;display:flex;align-items:center;justify-content:center;flex:none}
.footer-rule{left:112px;top:297px;width:976px;height:1px;background:#555}
.social{left:112px;top:318px;display:flex;gap:8px}
.social span{width:41px;height:41px;border:2px solid var(--white);border-radius:50%}
.copyright{right:112px;top:328px;font-size:17px}
</style>
</head>
<body>

<header class="site-header">
  <div class="brand"><span class="brand-dot"></span>PLEXUMAR</div>
  <nav class="main-nav">
    <a class="active" style="left:654px">Home</a>
    <a style="left:739px">Our Services</a>
    <a style="left:884px">About Us</a>
    <a style="left:997px">Contact Us</a>
  </nav>
</header>

<section class="hero">
  <div class="hero-photo" role="img" aria-label="Hero photo: a hand holding a glowing digital network"></div>
  <svg class="hero-curve" width="1200" height="740" viewBox="0 0 1200 740">
    <path d="M0 614 Q600 857 1200 614 L1200 740 L0 740 Z" fill="#2478c4"/>
    <path d="M0 620 Q600 850 1200 614 L1200 740 L0 740 Z" fill="#ffffff"/>
  </svg>
  <h1 class="hero-title">PLEXUMAR</h1>
  <p class="hero-sub">NAVIGATING BUSINESS &amp;<br>TECHNOLOGY TO GENERATE RESULTS</p>
  <a class="btn">Get Started</a>
  <div class="slider-dots"><span></span><span class="on"></span><span></span></div>
</section>

<section class="about">
  <h2 class="heading abs about-heading">ABOUT <em>PLEXUMAR</em></h2>
  <div class="rule abs"></div>
  <div class="about-copy abs">
    <p>Plexumar was formed in late 2018 to bring over 35 years of experience in multiple industries and disciplines to our customers. Dale Fenwick has led large and small organizations. With senior executive experience in business and technology, he has a distinct view of the business and technology needs of organizations.</p>
    <p>Dale has spent the last 20 years in various senior leadership positions at a leading property &amp; casualty insurance group, most recently as Chairman and President. He spent the early years of his career in high-tech manufacturing.</p>
  </div>
  <a class="btn">Read More</a>
  <svg class="portrait-frame abs" width="490" height="505" viewBox="0 0 490 505">
    <g fill="none" stroke="#2478c4" stroke-width="3">
      <path d="M2 70 V2 H82"/><path d="M406 2 H488 V70"/>
      <path d="M2 433 V503 H82"/><path d="M406 503 H488 V433"/>
    </g>
  </svg>
  <div class="portrait abs" role="img" aria-label="Portrait photo of the company founder"></div>
</section>

<section class="services abs">
  <h2 class="heading abs services-heading">OUR <em>SERVICES</em></h2>
  <div class="rule blue abs"></div>
  <svg width="1200" height="877" viewBox="0 0 1200 877">
    <circle cx="600" cy="483" r="255" fill="none" stroke="#cdd6df" stroke-width="1"/>
    <g stroke="#2478c4" stroke-width="3">
      <line x1="600" y1="483" x2="602" y2="240"/>
      <line x1="600" y1="483" x2="424" y2="313"/>
      <line x1="600" y1="483" x2="798" y2="333"/>
      <line x1="600" y1="483" x2="346" y2="497"/>
      <line x1="600" y1="483" x2="848" y2="495"/>
      <line x1="600" y1="483" x2="407" y2="653"/>
      <line x1="600" y1="483" x2="782" y2="652"/>
      <line x1="600" y1="483" x2="602" y2="737"/>
    </g>
    <circle cx="600" cy="483" r="152" fill="#2478c4"/>
    <circle cx="602" cy="240" r="52" fill="#2478c4"/>
    <g fill="#fff" stroke="#2478c4" stroke-width="2">
      <circle cx="424" cy="313" r="51"/><circle cx="798" cy="333" r="51"/>
      <circle cx="346" cy="497" r="51"/><circle cx="848" cy="495" r="51"/>
      <circle cx="407" cy="653" r="51"/><circle cx="782" cy="652" r="51"/>
      <circle cx="602" cy="737" r="51"/>
    </g>
    <g fill="none" stroke="#fff" stroke-width="2.5">
      <rect x="594" y="216" width="16" height="14"/><path d="M602 230 V238 M584 238 H620 M584 238 V244 M602 238 V244 M620 238 V244"/>
      <rect x="576" y="244" width="16" height="14"/><rect x="594" y="244" width="16" height="14"/><rect x="612" y="244" width="16" height="14"/>
    </g>
    <g fill="none" stroke="#2478c4" stroke-width="2">
      <rect x="404" y="295" width="40" height="36" rx="2"/><circle cx="430" cy="318" r="7"/><path d="M412 325 V310 M418 325 V304"/>
      <rect x="776" y="314" width="44" height="36" rx="2"/><path d="M776 322 H820"/><circle cx="796" cy="337" r="7"/>
      <rect x="326" y="476" width="14" height="14"/><rect x="352" y="476" width="14" height="14"/><rect x="326" y="504" width="14" height="14"/><rect x="352" y="504" width="14" height="14"/><path d="M340 483 H352 M340 511 H352 M333 490 V504 M359 490 V504"/>
      <rect x="830" y="472" width="32" height="44" rx="2"/><path d="M838 484 H854 M838 494 H854 M838 504 H848"/><circle cx="862" cy="508" r="8"/><path d="M858 508 l3 3 5 -6"/>
      <rect x="385" y="633" width="44" height="32" rx="2"/><path d="M407 665 V675 M397 675 H417 M393 658 V650 M399 658 V644 M405 658 V647 M411 658 V640"/>
      <path d="M782 628 l20 8 v14 c0 14 -10 22 -20 26 c-10 -4 -20 -12 -20 -26 v-14 z"/><path d="M772 650 l7 7 12 -14"/>
      <path d="M588 715 h20 l10 10 v34 h-30 z"/><circle cx="608" cy="748" r="8"/><path d="M614 754 l8 8"/>
    </g>
    <text x="600" y="495" text-anchor="middle" style="font-size:34px;font-weight:700;fill:#fff">PLEXUMAR</text>
    <g text-anchor="middle">
      <text x="601" y="171">BUSINESS &amp; TECHNOLOGY STRATEGY</text>
      <text x="282" y="299">PRODUCT</text><text x="282" y="322">DEVELOPMENT</text>
      <text x="974" y="314">DISTRIBUTION</text><text x="974" y="337">CHANNEL DEVELOPMENT</text>
      <text x="186" y="494">TECHNOLOGY</text><text x="186" y="517">IMPLEMENTATION</text>
      <text x="240" y="663">DATA/REPORTING/</text><text x="240" y="686">ANALYTICS</text>
      <text x="950" y="661">INSURANCE</text><text x="950" y="684">OPERATIONS/PROCESS</text>
      <text x="602" y="817">M &amp; A DUE DILIGENCE</text>
    </g>
    <text x="918" y="502">RATING &amp; REGULATORY</text>
  </svg>
</section>

<section class="contact">
  <h2 class="heading abs contact-heading">CONTACT <em>US</em></h2>
  <div class="rule blue abs"></div>
  <p class="contact-intro abs">If you have any questions or requests about our company or the services we provide, please call or<br>email us, or use the form below.</p>
  <div class="field" style="left:260px;top:2607px;width:335px;height:50px">First Name :</div>
  <div class="field" style="left:606px;top:2607px;width:335px;height:50px">Last Name :</div>
  <div class="field" style="left:260px;top:2674px;width:335px;height:50px">Company :</div>
  <div class="field" style="left:606px;top:2674px;width:335px;height:50px">Email :</div>
  <div class="field" style="left:260px;top:2738px;width:678px;height:50px">Subject :</div>
  <div class="field area" style="left:260px;top:2801px;width:678px;height:127px">How can we help you?</div>
  <a class="btn">Submit</a>
</section>

<footer class="site-footer abs">
  <div class="footer-brand abs"><span class="brand-dot"></span>PLEXUMAR</div>
  <nav class="footer-nav abs">
    <a style="left:369px">HOME</a>
    <a style="left:465px">OUR SERVICES</a>
    <a style="left:620px">ABOUT US</a>
    <a style="left:743px">CONTACT US</a>
  </nav>
  <div class="info abs" style="left:196px;top:220px">
    <span class="ring"><svg width="14" height="18" viewBox="0 0 14 18"><path d="M7 0a7 7 0 0 1 7 7c0 5-7 11-7 11S0 12 0 7a7 7 0 0 1 7-7z" fill="#fff"/><circle cx="7" cy="7" r="2.5" fill="#232323"/></svg></span>
    <span>42 Harbor Ridge Way<br>Lakeview, NV 89000</span>
  </div>
  <div class="info abs" style="left:521px;top:220px">
    <span class="ring"><svg width="16" height="16" viewBox="0 0 16 16"><path d="M3 1l3 3-2 2c1 2 3 4 6 6l2-2 3 3-2 2C7 15 1 9 1 3z" fill="#fff"/></svg></span>
    <span>555-014-2738</span>
  </div>
  <div class="info abs" style="left:757px;top:220px">
    <span class="ring"><svg width="18" height="14" viewBox="0 0 18 14"><rect width="18" height="14" rx="2" fill="#fff"/><path d="M1 2l8 6 8-6" fill="none" stroke="#232323" stroke-width="1.5"/></svg></span>
    <span>info@plexumar.example</span>
  </div>
  <div class="footer-rule abs"></div>
  <div class="social abs"><span></span><span></span><span></span></div>
  <p class="copyright abs">Copyrights © 2022.All rights reserved.</p>
</footer>

</body>
</html>
```